Driftwater

Club flyer, grand opening night, house/electronic music, looking for clean design with a sample image attached. Please look at the prior flyers to get an idea of the style. Guaranteed project
I would like to use the red design if possible (driftwater flyer attached)
Text:
DRIFTWATER
Winter House Music Monthly
Opening Night Dec 13 2013
Tessaline (use logo)
Featuring
BRONTIK (House/Garage)
(use logo with just Brontik name)
w/ resident
ZEV (Pinwheel)
Free All Night
Target Market(s)
21-39 year old club with all house/electronic music. classier and grown up over gimmicky
Industry/Entity Type
Club
Look and feel

```html
<!DOCTYPE html>
<html lang="en">
<head>
<meta charset="utf-8">
<title>Driftwater — Winter House Music Monthly</title>
<link rel="stylesheet" href="https://fonts.googleapis.com/css2?family=Cinzel:wght@700;900&family=Questrial&display=swap">
<style>
  :root {
    --backdrop: #141a1a;
    --paper: #ffffff;
    --title-pink: #e8175d;
    --ink: #111111;
    --headline-white: #ffffff;
    --hero-red: #e0204f;
    --hero-magenta: #d1246b;
    --hero-orange: #f2a23a;
    --hero-amber: #f6c96a;
    --hero-mist: #eeeeee;
    --crowd-black: #050505;
  }
  html, body {
    margin: 0;
    padding: 0;
    width: 1038px;
    height: 1200px;
    overflow: hidden;
    background: var(--backdrop);
  }
  .canvas {
    position: relative;
    width: 1038px;
    height: 1200px;
  }
  .flyer {
    position: absolute;
    left: 86px;
    top: 40px;
    width: 866px;
    height: 1120px;
    background: var(--paper);
    overflow: hidden;
  }
  .hero-art {
    position: absolute;
    left: 0;
    top: 210px;
    width: 866px;
    height: 910px;
    background:
      radial-gradient(ellipse 300px 280px at 420px 240px, var(--hero-red) 0%, var(--hero-magenta) 45%, rgba(209,36,107,0) 100%),
      radial-gradient(ellipse 340px 320px at 650px 300px, var(--hero-amber) 0%, var(--hero-orange) 40%, rgba(242,162,58,0) 100%),
      linear-gradient(to bottom, var(--hero-mist) 0%, #e4e0dc 45%, #b8a7a0 62%, var(--crowd-black) 82%, var(--crowd-black) 100%);
  }
  .masthead {
    position: absolute;
    left: 0;
    top: 82px;
    width: 866px;
    text-align: center;
  }
  .event-name {
    margin: 0;
    font-family: "Questrial", sans-serif;
    font-weight: 400;
    font-size: 84px;
    line-height: 1;
    letter-spacing: 9px;
    color: var(--title-pink);
    -webkit-text-stroke: 1.5px var(--title-pink);
  }
  .series-name {
    margin: 10px 0 0;
    font-family: "Cinzel", serif;
    font-weight: 900;
    font-size: 36px;
    line-height: 1;
    letter-spacing: 1px;
    color: var(--ink);
  }
  .headline {
    position: absolute;
    left: 0;
    width: 866px;
    text-align: center;
    font-family: "Cinzel", serif;
    font-weight: 900;
    color: var(--headline-white);
    text-shadow:
      -2px -2px 0 var(--ink), 2px -2px 0 var(--ink),
      -2px 2px 0 var(--ink), 2px 2px 0 var(--ink),
      0 3px 6px rgba(0,0,0,0.5);
  }
  .opening {
    top: 440px;
    font-size: 44px;
    line-height: 50px;
  }
  .admission {
    top: 604px;
    font-size: 40px;
    line-height: 56px;
  }
  .lineup {
    position: absolute;
    left: 0;
    top: 999px;
    width: 866px;
    height: 91px;
  }
  .act {
    position: absolute;
    top: 0;
    width: 220px;
    height: 91px;
    background: var(--paper);
    border-radius: 3px;
    display: flex;
    align-items: center;
    justify-content: center;
    font-family: "Cinzel", serif;
    font-weight: 900;
    color: var(--ink);
  }
  .act-host { left: 47px; font-size: 25px; }
  .act-feature { left: 323px; font-size: 30px; letter-spacing: 1px; }
  .act-resident { left: 593px; font-size: 16px; }
</style>
</head>
<body>
<main class="canvas">
  <article class="flyer">
    <div class="hero-art" role="img" aria-label="Collage of a chrome vintage microphone over a red paint burst and warm stage light, club word typography in the background, and a silhouetted crowd with raised hands around a performer"></div>

    <header class="masthead">
      <h1 class="event-name">DRIFTWATER</h1>
      <p class="series-name">Winter House Music Monthly</p>
    </header>

    <p class="headline opening">Opening Night<br>Dec 13 2013</p>
    <p class="headline admission">Free<br>All Night</p>

    <section class="lineup">
      <div class="act act-host">Tessaline</div>
      <div class="act act-feature">BRONTIK</div>
      <div class="act act-resident">ZEV (Pinwheel)</div>
    </section>
  </article>
</main>
</body>
</html>
```